Paws About Town Helpers

Design a flyer (A5 - I think!) with bright colours to promote an in home Dog Service.
Include an animated picture of a dog (being walked/playing/jumping etc)
Bold Heading, list of services with animated pictures, contact details

Industry/Entity Type

It Service

Requirements
Must have
• Add price list to back of A5 Flyer with same colours and design as front page of flyer - See Attached.

```html
<!DOCTYPE html>
<html lang="en">
<head>
<meta charset="utf-8">
<title>Paws About Town Helpers – Flyer</title>
<link href="https://fonts.googleapis.com/css2?family=PT+Sans:ital,wght@0,400;0,700;1,400&display=swap" rel="stylesheet">
<style>
  :root {
    --page-bg: #e9e7e4;
    --white: #ffffff;
    --sky: #7391cd;
    --navy: #3b55a7;
    --lilac: #b9c3ea;
    --orange: #ec8c2f;
    --yellow: #f9c723;
    --link-blue: #5a7cc6;
    --coat-light: #f1dcb0;
    --coat-dark: #c99a5a;
  }
  * { box-sizing: border-box; margin: 0; padding: 0; }
  html, body {
    width: 873px; height: 1200px; overflow: hidden;
    background: var(--page-bg);
    font-family: "PT Sans", Arial, sans-serif;
  }
  .flyer {
    position: absolute; left: 73px; top: 85px;
    width: 722px; height: 1022px; overflow: hidden;
    background: var(--sky);
    box-shadow: 0 4px 14px rgba(0,0,0,.25);
  }
  .flyer-backdrop { position: absolute; inset: 0; }
  .site-url {
    position: absolute; right: 26px; top: 30px;
    color: var(--link-blue); font-weight: 700; font-size: 18px;
  }
  .mascot {
    position: absolute; left: 60px; top: 32px; width: 152px; height: 200px;
    border-radius: 46% 46% 30% 30%;
    background: radial-gradient(circle at 50% 40%, #ffd84a, #f2b91c);
  }
  .headline {
    position: absolute; left: 221px; top: 102px; color: var(--orange);
  }
  .headline .kicker { display: block; font-size: 33px; font-weight: 400; line-height: 1; }
  .headline .brand { display: block; font-size: 37px; font-weight: 700; line-height: 1.2; margin-top: 4px; }
  .heart-badge { position: absolute; left: 493px; top: 232px; width: 128px; height: 108px; }
  .services { position: absolute; left: 50px; top: 323px; width: 660px; list-style: none; }
  .service { position: relative; padding-left: 84px; }
  .service-icon {
    position: absolute; left: 0; top: 4px; width: 60px; height: 60px;
    border-radius: 50%; background: var(--white); border: 3px solid var(--orange);
  }
  .service-icon::after {
    content: ""; position: absolute; inset: 14px; border-radius: 50%; background: var(--orange);
  }
  .service h2 { color: var(--white); font-size: 20px; font-weight: 700; line-height: 1.2; text-transform: uppercase; }
  .service p { color: var(--yellow); font-size: 19px; font-weight: 700; line-height: 1.25; }
  .service:nth-child(1) { height: 95px; }
  .service:nth-child(2) { height: 86px; }
  .service:nth-child(3) { height: 80px; }
  .service:nth-child(4) { height: 90px; }
  .paw-mark {
    position: absolute; width: 64px; height: 56px; border-radius: 40%;
    background: rgba(185,195,234,.55);
  }
  .photo { position: absolute; }
  .photo-puppy {
    left: 22px; top: 728px; width: 160px; height: 246px; border-radius: 42% 42% 20% 20%;
    background: linear-gradient(180deg, var(--coat-light), var(--coat-dark));
  }
  .photo-pair {
    left: 322px; top: 722px; width: 396px; height: 224px; border-radius: 40% 40% 8% 8%;
    background: linear-gradient(160deg, var(--coat-light), var(--coat-dark));
  }
  .footer-band {
    position: absolute; left: 0; bottom: 0; width: 100%; height: 86px;
    background: var(--orange); color: var(--white); text-align: right; padding: 12px 24px 0 0;
  }
  .footer-band .tagline { font-size: 17px; font-weight: 700; text-transform: uppercase; letter-spacing: .2px; }
  .footer-band .call { display: flex; justify-content: flex-end; align-items: center; gap: 8px; margin-top: 2px; }
  .call-label { font-size: 22px; font-weight: 700; }
  .call-name { font-size: 21px; font-style: italic; font-weight: 400; }
  .call-icon { width: 28px; height: 28px; margin-left: 6px; }
  .call-number { font-size: 27px; font-weight: 700; }
</style>
</head>
<body>
<main class="flyer">
  <svg class="flyer-backdrop" viewBox="0 0 722 1022" aria-hidden="true">
    <rect width="722" height="1022" fill="var(--sky)"/>
    <path d="M0 760 C 150 840, 500 740, 722 650 L722 1022 L0 1022 Z" fill="var(--navy)"/>
    <path d="M0 640 C 40 720, 120 745, 280 745 C 460 745, 620 700, 722 650 L722 660 C 620 712, 460 758, 280 758 C 110 758, 30 735, 0 660 Z" fill="var(--lilac)"/>
    <path d="M0 0 H722 V120 C 690 220, 560 292, 300 298 C 120 300, 20 240, 0 150 Z" fill="var(--yellow)"/>
    <path d="M0 0 H722 V108 C 690 205, 560 276, 300 282 C 120 284, 24 228, 0 138 Z" fill="var(--white)"/>
  </svg>

  <div class="site-url">www.pawsabouttownhelpers.com.au</div>
  <div class="mascot" role="img" aria-label="Cartoon yellow puppy with a blue collar, sitting and smiling"></div>

  <h1 class="headline">
    <span class="kicker">WE ARE:</span>
    <span class="brand">Paws About Town Helpers</span>
  </h1>

  <svg class="heart-badge" viewBox="0 0 128 108" aria-hidden="true">
    <path d="M64 106 C 20 74, 0 52, 0 30 C 0 12, 14 0, 32 0 C 46 0, 58 8, 64 20 C 70 8, 82 0, 96 0 C 114 0, 128 12, 128 30 C 128 52, 108 74, 64 106 Z" fill="var(--orange)"/>
    <g fill="var(--white)">
      <ellipse cx="64" cy="62" rx="17" ry="14"/>
      <ellipse cx="44" cy="42" rx="7" ry="9"/>
      <ellipse cx="57" cy="32" rx="7" ry="9"/>
      <ellipse cx="71" cy="32" rx="7" ry="9"/>
      <ellipse cx="84" cy="42" rx="7" ry="9"/>
    </g>
  </svg>

  <div class="paw-mark" role="img" aria-label="Faint paw print" style="left:638px;top:382px"></div>
  <div class="paw-mark" role="img" aria-label="Faint paw print" style="left:606px;top:464px"></div>
  <div class="paw-mark" role="img" aria-label="Faint paw print" style="left:642px;top:560px"></div>
  <div class="paw-mark" role="img" aria-label="Faint paw print" style="left:596px;top:652px"></div>

  <ul class="services">
    <li class="service">
      <span class="service-icon" role="img" aria-label="Dog poop icon"></span>
      <h2>Tired of picking up dog poop?</h2>
      <p>- arrange for us to do it for you!</p>
    </li>
    <li class="service">
      <span class="service-icon" role="img" aria-label="Dog on a lead icon"></span>
      <h2>Need a break from walking the dog?</h2>
      <p>- we will come and collect your dog and take it for a walk!</p>
    </li>
    <li class="service">
      <span class="service-icon" role="img" aria-label="Dog food bowl icon"></span>
      <h2>Can’t get home in time to feed your dog?</h2>
      <p>- use our dog feeding service!</p>
    </li>
    <li class="service">
      <span class="service-icon" role="img" aria-label="Tennis ball icon"></span>
      <h2>Want someone to play with your dog while you’re at work?</h2>
      <p>- we will be Paws About Town Helpers!</p>
    </li>
    <li class="service">
      <span class="service-icon" role="img" aria-label="Bathtub icon"></span>
      <h2>Dog needs a bath?</h2>
      <p>- we’ll arrange for a professional to keep it clean!</p>
    </li>
  </ul>

  <div class="photo photo-puppy" role="img" aria-label="Photo of a golden retriever puppy sitting"></div>
  <div class="photo photo-pair" role="img" aria-label="Photo of a golden retriever lying down beside a cocker spaniel"></div>

  <footer class="footer-band">
    <div class="tagline">For all services related to your dog</div>
    <div class="call">
      <span class="call-label">CALL NOW</span>
      <span class="call-name">Paws About Town Helpers</span>
      <svg class="call-icon" viewBox="0 0 28 28" aria-hidden="true">
        <circle cx="14" cy="14" r="12.5" fill="none" stroke="var(--white)" stroke-width="2"/>
        <path d="M9.5 7.5 L12 7 L13.2 10.6 L11.6 12 C 12.4 13.8 14 15.6 16 16.4 L17.4 14.8 L21 16 L20.5 18.6 C 14 19.5 8.5 14 9.5 7.5 Z" fill="var(--white)"/>
      </svg>
      <span class="call-number">0400 318 527</span>
    </div>
  </footer>
</main>
</body>
</html>
```